Business Card Design Project

We need a business card to reflect the design of our website - just so it all ties in - it has a retro feel and can be found at http://www.velorasoulpair.com
We will need our phone 0437 215 964
Web address, and email velorapair@fernmail.com included
Our catch cry is "Classic Cocktail Music"
Perfect Live Music for Private & Corporate Events, Weddings and Dinner Music
Our names should be included :-
Maribel Thorne / piano & Dennis Holloway / bass
I am now also including our logo so that it can be included (in part or whole) somehow in the design
My partner thinks we should include our logo in some form in the design of the card - i will attach this here for you. I will attach eps but if you prefer another format please let me know
Regards
Mari

```html
<!DOCTYPE html>
<html lang="en">
<head>
<meta charset="utf-8">
<title>Velora Pair – Business Card</title>
<link rel="stylesheet" href="https://fonts.googleapis.com/css2?family=Federo&family=Gelasio:wght@400&display=swap">
<style>
  :root {
    --stage: #2a2a2a;
    --card: #80b9b8;
    --card-edge: #6ea7a6;
    --stitch: #4f7f80;
    --rule: #2f3b3b;
    --cream: #f4e8c8;
    --ink: #2f3434;
    --badge: #474747;
    --clef-wood: #6b4b35;
    --clef-cream: #efe2c4;
  }
  * { margin: 0; padding: 0; box-sizing: border-box; }
  html, body { width: 1200px; height: 1050px; overflow: hidden; }
  body { background: var(--stage); position: relative; font-family: "Gelasio", Georgia, serif; }

  .card {
    position: absolute;
    background: var(--card);
    border: 2px solid var(--card-edge);
  }
  .card--front { left: 473px; top: 76px; width: 623px; height: 358px; }
  .card--back  { left: 473px; top: 561px; width: 624px; height: 357px; }

  .stitch {
    position: absolute; inset: 12px;
    border: 1px dashed var(--stitch);
  }
  .frame {
    position: absolute; left: 23px; top: 23px; right: 23px; bottom: 21px;
    border: 1px solid var(--rule);
  }

  .card__name {
    position: absolute; left: 40px; top: 30px;
    font-family: "Federo", sans-serif; font-weight: 400;
    font-size: 56px; letter-spacing: 0;
    color: var(--cream); line-height: 1; white-space: nowrap;
  }
  .card__tagline {
    position: absolute; left: 96px; top: 94px;
    font-size: 25px; letter-spacing: 0.8px; color: var(--cream); line-height: 1;
  }
  .card__services {
    position: absolute; left: 34px; top: 123px;
    font-size: 25px; letter-spacing: 0.5px; color: var(--cream); line-height: 31px;
  }
  .card__contact {
    position: absolute; left: 34px; top: 240px;
    font-size: 20.5px; color: var(--ink); line-height: 26px;
  }

  .badge {
    position: absolute; border-radius: 50%;
    background: var(--badge);
    display: flex; align-items: center; justify-content: center;
    color: var(--cream); font-family: "Gelasio", Georgia, serif;
  }
  .badge--small { left: 289px; top: 184px; width: 82px; height: 82px; font-size: 13px; border: 2px solid var(--stitch); }
  .badge--large { left: 221px; top: 96px; width: 166px; height: 166px; font-size: 26px; border: 3px solid #5d6b6b; box-shadow: inset 0 0 0 4px var(--badge), inset 0 0 0 5px #8a8a8a; }

  .card__players {
    position: absolute; left: 0; right: 0; top: 288px;
    text-align: center; font-size: 15px; color: var(--ink); line-height: 1;
  }

  .clef-art {
    position: absolute; left: 404px; top: 24px; width: 190px; height: 310px;
  }
</style>
</head>
<body>
  <section class="card card--front">
    <div class="stitch"></div>
    <div class="frame"></div>
    <h1 class="card__name">VELORA PAIR</h1>
    <p class="card__tagline">Classic Cocktail Music</p>
    <p class="card__services">Perfect Live Music for Private<br>&amp; Corporate Events, Weddings<br>and Dinner Music</p>
    <div class="badge badge--small">Velora Pair</div>
    <p class="card__contact">tél: 0437 215 964<br>Email:velorapair@fernmail.com<br>site web: www.velorasoulpair.com</p>
    <svg class="clef-art" viewBox="0 0 190 310" role="img" aria-label="Wood-grain treble clef with cream flourish ornaments">
      <defs>
        <linearGradient id="clefTone" x1="0" y1="0" x2="1" y2="1">
          <stop offset="0" stop-color="#efe2c4" stop-opacity="0.55"/>
          <stop offset="0.5" stop-color="#6b4b35" stop-opacity="0.75"/>
          <stop offset="1" stop-color="#efe2c4" stop-opacity="0.55"/>
        </linearGradient>
      </defs>
      <rect width="190" height="310" fill="url(#clefTone)"/>
    </svg>
  </section>

  <section class="card card--back">
    <div class="stitch"></div>
    <div class="badge badge--large">Velora Pair</div>
    <p class="card__players">Maribel Thorne / piano &nbsp;·&nbsp; Dennis Holloway / bass</p>
  </section>
</body>
</html>
```